Hackthon event need a Landing Page

We are looking for a landing page to represent an event we are preparing in our country (Dominican Republic), it would be the first of this type, and we want to create a positive impact and make it a brand to make it recurring year to year .

The event is a hackathon where we will be gathering students and professionals to solve challenges using software development.

This landing page should be resposive, multi-language, clean, modern and align with the event logo.

Find a good example of what we are looking for in the following link:

https://brightcodefest.example/

We would like to have the following sections(Not necesarily in this order, not necesarily all of them):

- Brief
- Agenda
- Countdown
- Form Button to redirect to the event registration service.
---> Note: We would like to see the option of having the form in the landing page.
- Contact info and Social Media
- Partners/Sponsors
- Link to intro video

We will be attaching the logo and the variations of colors we are looking to see. It should be with a black background

```html
<!DOCTYPE html>
<html lang="en">
<head>
<meta charset="utf-8">
<title>Bright Code Fest — Hackathon</title>
<link rel="stylesheet" href="https://fonts.googleapis.com/css2?family=Exo+2:wght@400;500&family=Raleway:wght@400;500&display=swap">
<style>
:root{
  --bg:#1d1c2c;
  --bg-alt:#222133;
  --panel:#2a2939;
  --coral:#f47c6c;
  --teal:#1fd8c0;
  --blue:#2a9df4;
  --white:#ffffff;
  --muted:#c9c8d4;
  --line:#3a394c;
  --head:"Exo 2",sans-serif;
  --body:"Raleway",sans-serif;
}
*{box-sizing:border-box;margin:0;padding:0}
html,body{width:1200px;height:4168px;overflow:hidden}
body{background:var(--bg);color:var(--white);font-family:var(--body);position:relative}
.abs{position:absolute}
a{color:inherit;text-decoration:none}

/* header */
.topbar{top:12px;right:100px;display:flex;gap:18px;align-items:center;font-size:15px}
.dot-icon{width:12px;height:12px;border-radius:50%;background:var(--white);display:inline-block}
.brand{top:40px;left:104px;display:flex;align-items:center;gap:10px;font-family:var(--head);font-size:22px;font-weight:500;color:var(--coral)}
.brand .mark{width:16px;height:16px;border-radius:50%;background:var(--coral)}
.nav{top:72px;left:572px;display:flex;gap:44px;font-family:var(--head);font-size:18px}
.nav a.active{color:var(--coral);position:relative}
.nav a.active::after{content:"";position:absolute;left:50%;top:32px;width:7px;height:7px;margin-left:-3px;border-radius:50%;background:var(--coral)}
.nav-rule{top:106px;left:1010px;width:190px;height:1px;background:var(--line)}
.lang-flag{display:inline-block;width:20px;height:12px;background:var(--muted);margin-right:8px;vertical-align:middle}

/* hero */
.hero-photo{top:0;left:0;width:1200px;height:760px;background:linear-gradient(180deg,#2c2c3e 0%,#262538 55%,var(--bg) 100%)}
.hero-kicker{top:236px;left:99px;font-family:var(--head);font-size:32px}
.hero-title{top:282px;left:99px;font-family:var(--head);font-size:72px;line-height:78px;font-weight:500}
.btn{display:flex;align-items:center;justify-content:flex-start;background:var(--coral);color:#1d1c2c;font-family:var(--head);font-size:17px;clip-path:polygon(0 0,100% 0,88% 100%,0 100%)}
.btn-hero{top:462px;left:99px;width:220px;height:44px;padding-left:18px}
.hero-emblem{top:160px;left:660px;width:426px;height:426px;display:flex;align-items:center;justify-content:center;gap:14px;font-family:var(--head);font-size:42px;font-weight:500;color:var(--coral)}
.hero-emblem .mark{width:26px;height:26px;border-radius:50%;background:var(--coral);flex:none}

/* welcome */
.welcome-title{top:856px;left:99px;font-family:var(--head);font-size:50px;line-height:62px;color:var(--teal)}
.welcome-text{top:990px;left:99px;width:580px;font-size:17px;line-height:34px;color:var(--muted)}
.btn-read{top:1185px;left:99px;width:204px;height:52px;padding-left:34px}
.enquiry{top:820px;left:700px;width:401px;height:467px;background:var(--panel);padding:22px 24px}
.enquiry h2{font-family:var(--head);font-weight:400;font-size:34px;margin-bottom:22px}
.field{display:block;width:353px;height:42px;background:var(--white);color:#777;font-size:16px;padding:10px 12px;margin-bottom:15px}
.btn-submit{width:180px;height:48px;padding-left:48px;margin-top:6px}

/* agenda */
.agenda{top:1405px;left:142px;width:920px;height:746px;background:var(--bg-alt)}
.agenda-title{top:1432px;left:0;width:1200px;text-align:center;font-family:var(--head);font-size:54px;color:var(--teal);text-shadow:0 0 14px rgba(31,216,192,.5)}
.agenda-intro{top:1505px;left:190px;width:820px;text-align:center;font-size:17px;line-height:27px;color:var(--muted)}
.day h3{font-family:var(--head);font-weight:400;font-size:33px}
.day .date{color:var(--teal);font-size:17px;margin-top:2px}
.day table{border-collapse:collapse;margin-top:24px;font-size:17px}
.day td{height:41px;vertical-align:top;padding-top:6px}
.day td.time{text-align:right;padding-right:16px;width:112px;border-right:1px solid var(--line)}
.day td.item{padding-left:16px}

/* video */
.video{top:2335px;left:99px;width:1002px;height:553px;background:linear-gradient(135deg,#d9d6d1 0%,#b9b4ad 50%,#8e8881 100%)}
.play{top:2581px;left:570px;width:60px;height:60px;border-radius:50%;background:var(--coral)}

/* countdown */
.band{top:3020px;left:0;width:1200px;height:740px;background:var(--bg-alt)}
.count-title{top:3058px;left:0;width:1200px;text-align:center;font-family:var(--head);font-size:54px;color:var(--teal)}
.counter{top:3150px;width:156px;text-align:center}
.counter .num{position:absolute;top:0;left:0;width:156px;height:156px;display:flex;align-items:center;justify-content:center;font-family:var(--head);font-size:52px}
.counter .lbl{position:absolute;top:172px;left:0;width:156px;font-size:17px;color:var(--muted)}
.partners-title{top:3450px;left:0;width:1200px;text-align:center;font-family:var(--head);font-size:54px;color:var(--teal)}
.partners{top:3560px;left:170px;width:860px;display:flex;justify-content:space-between}
.partner{width:104px;height:112px;border:3px solid var(--white);border-radius:50%}
.partner.sq{border-radius:12px}

/* footer */
.footer-brand{top:3880px;left:100px;display:flex;align-items:center;gap:10px;font-family:var(--head);font-size:22px;font-weight:500;color:var(--coral)}
.footer-brand .mark{width:16px;height:16px;border-radius:50%;background:var(--coral)}
.fdiv{top:3811px;width:1px;height:248px;background:var(--line)}
.fdiv::before{content:"";position:absolute;top:26px;left:-2px;width:4px;height:24px;background:var(--teal)}
.fcol h4{font-family:var(--head);font-weight:400;font-size:20px;color:var(--teal)}
.fcol .rule{width:40px;height:1px;background:var(--coral);margin:10px 0 22px;position:relative}
.fcol .rule::after{content:"";position:absolute;right:0;top:-3px;width:7px;height:7px;border-radius:50%;background:var(--coral)}
.fcol li{list-style:none;font-size:17px;color:var(--muted);margin-bottom:23px}
.contact li{display:flex;gap:12px;margin-bottom:14px;line-height:26px}
.contact svg{flex:none;margin-top:5px}
.socials{display:flex;gap:22px}
.footer-rule{top:4107px;left:97px;width:1006px;height:1px;background:var(--line)}
.copy{top:4128px;left:0;width:1200px;text-align:center;font-size:13px;color:#8a8998}
.copy span{color:var(--coral)}
</style>
</head>
<body>

<!-- hero -->
<div class="abs hero-photo" role="img" aria-label="Darkened photo of smiling developers working together at a hackathon"></div>

<div class="abs topbar">
  <span class="dot-icon" aria-label="Social network"></span>
  <span class="dot-icon" aria-label="Social network"></span>
  <span class="dot-icon" aria-label="Social network"></span>
  <span><svg width="14" height="14" viewBox="0 0 24 24"><path fill="#f47c6c" d="M6.6 10.8a15 15 0 0 0 6.6 6.6l2.2-2.2c.3-.3.7-.4 1-.2 1.1.4 2.3.6 3.6.6.6 0 1 .4 1 1V20c0 .6-.4 1-1 1A17 17 0 0 1 3 4c0-.6.4-1 1-1h3.5c.6 0 1 .4 1 1 0 1.3.2 2.5.6 3.6.1.3 0 .7-.2 1z"/></svg> 01 555 010 200</span>
</div>

<div class="abs brand"><span class="mark"></span>Bright Code Fest</div>

<nav class="abs nav">
  <a class="active" href="#">Home</a>
  <a href="#">Challenges</a>
  <a href="#">Agenda</a>
  <a href="#">Contact</a>
  <a href="#"><span class="lang-flag"></span>Eng ˅</a>
</nav>
<div class="abs nav-rule"></div>

<p class="abs hero-kicker">Solve challenges using</p>
<h1 class="abs hero-title">Software<br>Development</h1>
<a class="abs btn btn-hero" href="#">Event Registration</a>

<svg class="abs" style="top:154px;left:654px" width="438" height="438" viewBox="0 0 438 438">
  <circle cx="219" cy="219" r="210" fill="none" stroke="#f47c6c" stroke-width="3"/>
  <circle cx="219" cy="219" r="185" fill="none" stroke="#1fd8c0" stroke-width="1.5" stroke-dasharray="4 5"/>
</svg>
<div class="abs hero-emblem"><span class="mark"></span>Bright Code Fest</div>

<svg class="abs" style="top:0;left:0" width="1200" height="4168" viewBox="0 0 1200 4168" fill="none" stroke="#f47c6c" stroke-width="2">
  <polyline points="0,757 207,757 276,688"/><circle cx="281" cy="683" r="6"/>
  <polyline points="1200,1273 1101,1273"/>
  <polyline points="970,1289 914,1343"/><circle cx="910" cy="1347" r="6"/>
  <circle cx="606" cy="1593" r="6"/><polyline points="612,1593 1087,1593 1200,1701"/>
  <polyline points="0,2275 183,2275 255,2205"/><circle cx="259" cy="2201" r="6"/>
  <polyline points="0,2293 183,2293 226,2335"/>
  <polyline points="915,2888 993,2953 1200,2953"/>
</svg>

<!-- welcome -->
<h2 class="abs welcome-title">Welcome to<br>Bright Code Fest</h2>
<p class="abs welcome-text">Lorem ipsum dolor sit amet, consectetur adipiscing elit. Suspendisse vel dui sagittis, accumsan quam vitae, dignissim ante. Maecenas rutrum magna et porta scelerisque. Morbi moletie ac leo non maximus. Vivamus iaculis nibh vitae luctus vulputate. Phasellus a felis urna.</p>
<a class="abs btn btn-read" href="#">Read More</a>

<form class="abs enquiry">
  <h2>Quick Enquiry</h2>
  <span class="field">Name</span>
  <span class="field">Email</span>
  <span class="field">Phone</span>
  <span class="field">Location</span>
  <span class="field">Message</span>
  <span class="btn btn-submit">Submit</span>
</form>

<!-- agenda -->
<div class="abs agenda"></div>
<h2 class="abs agenda-title">Agenda</h2>
<p class="abs agenda-intro">Nulla hendrerit velit purus, imperdiet fermtum turpis vehicula sed. Cras in sem commodo, molestie eros egestas, dignissim purus. In at ex sit amet ex euismod vulputate quis sed urna.</p>

<div class="abs day" style="top:1630px;left:167px">
  <h3>Day 01</h3><p class="date">22.11.2022</p>
  <table>
    <tr><td class="time">9:30 - 10:30</td><td class="item">Lorem ipsum</td></tr>
    <tr><td class="time">10:30 - 12:30</td><td class="item">Dolor sit amet</td></tr>
    <tr><td class="time">15:30 - 17:30</td><td class="item">Consectetur</td></tr>
    <tr><td class="time">20:30 - 21:45</td><td class="item">Suspendiss</td></tr>
  </table>
</div>
<div class="abs day" style="top:1753px;left:467px">
  <h3>Day 02</h3><p class="date">22.11.2022</p>
  <table>
    <tr><td class="time">9:30 - 10:30</td><td class="item">Lorem ipsum</td></tr>
    <tr><td class="time">10:30 - 12:30</td><td class="item">Dolor sit amet</td></tr>
    <tr><td class="time">15:30 - 17:30</td><td class="item">Consectetur</td></tr>
    <tr><td class="time">20:30 - 21:45</td><td class="item">Suspendiss</td></tr>
  </table>
</div>
<div class="abs day" style="top:1868px;left:771px">
  <h3>Day 03</h3><p class="date">22.11.2022</p>
  <table>
    <tr><td class="time">9:30 - 10:30</td><td class="item">Lorem ipsum</td></tr>
    <tr><td class="time">10:30 - 12:30</td><td class="item">Dolor sit amet</td></tr>
    <tr><td class="time">15:30 - 17:30</td><td class="item">Consectetur</td></tr>
    <tr><td class="time">20:30 - 21:45</td><td class="item">Suspendiss</td></tr>
  </table>
</div>

<!-- video -->
<div class="abs video" role="img" aria-label="Intro video still: a team of young professionals gathered around a laptop at a table"></div>
<div class="abs play"></div>
<svg class="abs" style="top:2596px;left:590px" width="26" height="30" viewBox="0 0 26 30"><polygon points="2,0 26,15 2,30" fill="#ffffff"/></svg>

<!-- countdown -->
<div class="abs band"></div>
<h2 class="abs count-title">Countdown Timer</h2>

<svg class="abs" style="top:3150px;left:0" width="1200" height="160" viewBox="0 0 1200 160" fill="none" stroke-width="3">
  <circle cx="286" cy="78" r="76" stroke="#1fd8c0"/>
  <path d="M286 2 A76 76 0 0 1 362 78" stroke="#2a9df4" stroke-width="5"/>
  <circle cx="493" cy="78" r="76" stroke="#1fd8c0"/>
  <path d="M493 2 A76 76 0 0 1 547 132" stroke="#2a9df4" stroke-width="5"/>
  <circle cx="702" cy="78" r="76" stroke="#1fd8c0"/>
  <path d="M702 2 A76 76 0 1 1 646 129" stroke="#2a9df4" stroke-width="5"/>
  <circle cx="912" cy="78" r="76" stroke="#1fd8c0"/>
  <path d="M912 2 A76 76 0 0 1 948 145" stroke="#2fe0a8" stroke-width="5"/>
</svg>
<div class="abs counter" style="left:208px"><span class="num">7</span><span class="lbl">DAYS</span></div>
<div class="abs counter" style="left:415px"><span class="num">15</span><span class="lbl">HOURS</span></div>
<div class="abs counter" style="left:624px"><span class="num">48</span><span class="lbl">MINUTES</span></div>
<div class="abs counter" style="left:834px"><span class="num">24</span><span class="lbl">SECONDS</span></div>

<h2 class="abs partners-title">Partners</h2>
<svg class="abs" style="top:3600px;left:98px" width="28" height="54" viewBox="0 0 28 54"><polyline points="26,2 2,27 26,52" fill="none" stroke="#ffffff" stroke-width="2"/></svg>
<svg class="abs" style="top:3600px;left:1074px" width="28" height="54" viewBox="0 0 28 54"><polyline points="2,2 26,27 2,52" fill="none" stroke="#ffffff" stroke-width="2"/></svg>
<div class="abs partners">
  <span class="partner"></span><span class="partner sq"></span><span class="partner sq"></span>
  <span class="partner"></span><span class="partner sq"></span><span class="partner"></span>
</div>

<!-- footer -->
<div class="abs footer-brand"><span class="mark"></span>Bright Code Fest</div>
<div class="abs fdiv" style="left:333px"></div>
<div class="abs fdiv" style="left:572px"></div>
<div class="abs fdiv" style="left:909px"></div>

<div class="abs fcol" style="top:3826px;left:398px">
  <h4>Quick Links</h4><div class="rule"></div>
  <ul><li>Home</li><li>Challenges</li><li>Agenda</li><li>Contact</li></ul>
</div>

<div class="abs fcol contact" style="top:3826px;left:642px;width:240px">
  <h4>Contact Info</h4><div class="rule"></div>
  <ul>
    <li><svg width="14" height="16" viewBox="0 0 24 28"><path fill="#f47c6c" d="M12 0a10 10 0 0 0-10 10c0 7 10 18 10 18s10-11 10-18A10 10 0 0 0 12 0zm0 14a4 4 0 1 1 0-8 4 4 0 0 1 0 8z"/></svg><span>45 BC, making it over 2000</span></li>
    <li><svg width="15" height="12" viewBox="0 0 24 18"><rect width="24" height="18" rx="2" fill="#f47c6c"/><polyline points="1,2 12,10 23,2" fill="none" stroke="#222133" stroke-width="2"/></svg><span>info@brightcodefest.example</span></li>
    <li><svg width="14" height="14" viewBox="0 0 24 24"><path fill="#f47c6c" d="M6.6 10.8a15 15 0 0 0 6.6 6.6l2.2-2.2c.3-.3.7-.4 1-.2 1.1.4 2.3.6 3.6.6.6 0 1 .4 1 1V20c0 .6-.4 1-1 1A17 17 0 0 1 3 4c0-.6.4-1 1-1h3.5c.6 0 1 .4 1 1 0 1.3.2 2.5.6 3.6.1.3 0 .7-.2 1z"/></svg><span>01 555 010 200</span></li>
  </ul>
</div>

<div class="abs fcol" style="top:3826px;left:970px">
  <h4>Social Media</h4><div class="rule"></div>
  <div class="socials"><span class="dot-icon"></span><span class="dot-icon"></span><span class="dot-icon"></span></div>
</div>

<div class="abs footer-rule"></div>
<p class="abs copy">© 2022 <span>Bright Code Fest</span>. All right reserved</p>

</body>
</html>
```